Business Card Design

We would like a business card that utilizes our current logo and keeps with the same feel - elegant and organic. Our farm isn't about mass production, it's about excellence, education, beautiful events and flowers - people, culture, and community.

Target Market(s)

Patrons to our farm who are interested in weddings, events, or our flowers and vegetables.

Contact Information for Business Card

Name, address, cell email (Danielle Hoskins, 2716 Wrenfield Rd, Ashbury, CO 80417, cell 30.412.6638, email danielle@wrenfieldacres.com)

```html
<!DOCTYPE html>
<html lang="en">
<head>
<meta charset="utf-8">
<title>Wrenfield Acres — Business Card</title>
<link rel="stylesheet" href="https://fonts.googleapis.com/css2?family=Arimo:wght@400&display=swap">
<style>
  :root {
    --sage: #7b8c7b;
    --paper: #ffffff;
    --backdrop: #ffffff;
    --ink-soft: #7d7d7d;
    --card-w: 620px;
    --card-h: 354px;
  }
  * { box-sizing: border-box; margin: 0; padding: 0; }
  html, body {
    width: 780px;
    height: 1200px;
    overflow: hidden;
    background: var(--backdrop);
  }
  .canvas {
    position: relative;
    width: 780px;
    height: 1200px;
    font-family: "Arimo", Arial, sans-serif;
  }
  .card {
    position: absolute;
    left: 80px;
    width: var(--card-w);
    height: var(--card-h);
    overflow: hidden;
    background: var(--paper);
  }
  .card--front { top: 218px; }
  .card--back { top: 642px; }

  /* front: painted sage edges framing a white centre */
  .brush-edge {
    position: absolute;
    top: 0;
    height: 100%;
    width: 96px;
  }
  .brush-edge--left {
    left: 0;
    background: linear-gradient(to right, var(--sage) 0%, var(--sage) 62%, rgba(123,140,123,0.55) 80%, rgba(123,140,123,0) 100%);
  }
  .brush-edge--right {
    right: 0;
    background: linear-gradient(to left, var(--sage) 0%, var(--sage) 58%, rgba(123,140,123,0.55) 78%, rgba(123,140,123,0) 100%);
  }
  .wordmark {
    position: absolute;
    left: 0;
    right: 0;
    top: 150px;
    text-align: center;
    font-size: 30px;
    letter-spacing: 1px;
    color: var(--ink-soft);
  }

  /* back: sage field with white painted sides */
  .sage-field {
    position: absolute;
    inset: 0;
    background: linear-gradient(to right,
      rgba(123,140,123,0) 0px,
      rgba(123,140,123,0.5) 36px,
      var(--sage) 72px,
      var(--sage) calc(100% - 76px),
      rgba(123,140,123,0.5) calc(100% - 38px),
      rgba(123,140,123,0) 100%);
  }
  .contact {
    position: absolute;
    left: 192px;
    top: 112px;
    color: var(--paper);
    font-size: 19px;
    line-height: 1;
  }
  .contact__name {
    font-size: 22px;
    text-transform: uppercase;
    letter-spacing: 0.5px;
    margin-bottom: 24px;
  }
  .contact__line { margin-bottom: 15px; }
  .contact__row {
    display: flex;
    align-items: center;
    gap: 7px;
  }
  .contact__phone { font-size: 21px; margin-bottom: 22px; }
  .contact__email { font-size: 16px; }
  .contact__icon { width: 13px; height: 13px; flex: none; }
</style>
</head>
<body>
<main class="canvas">
  <section class="card card--front" aria-label="Business card front">
    <div class="brush-edge brush-edge--left" role="img" aria-label="Sage painted brush stroke along the left edge"></div>
    <div class="brush-edge brush-edge--right" role="img" aria-label="Sage painted brush stroke along the right edge"></div>
    <p class="wordmark">Wrenfield Acres</p>
  </section>

  <section class="card card--back" aria-label="Business card back">
    <div class="sage-field" role="img" aria-label="Sage painted field with white brushed sides"></div>
    <div class="contact">
      <p class="contact__name">Danielle Hoskins</p>
      <p class="contact__line">2716 Wrenfield Rd</p>
      <p class="contact__line">Ashbury, CO 80417</p>
      <p class="contact__row contact__phone">
        <svg class="contact__icon" viewBox="0 0 16 16" aria-hidden="true">
          <circle cx="8" cy="8" r="7" fill="none" stroke="#fff" stroke-width="1.3"/>
          <path d="M5 4.2l1.6-.4 1 2.1-1 .8c.5 1.1 1.2 1.8 2.2 2.3l.8-1 2.1 1-.4 1.6C7.8 10.8 5.2 8.2 5 4.2z" fill="#fff"/>
        </svg>
        <span>30.412.6638</span>
      </p>
      <p class="contact__row contact__email">
        <svg class="contact__icon" viewBox="0 0 16 16" aria-hidden="true">
          <rect x="1.5" y="3.5" width="13" height="9" fill="none" stroke="#fff" stroke-width="1.2"/>
          <path d="M1.5 3.5L8 9l6.5-5.5" fill="none" stroke="#fff" stroke-width="1.2"/>
        </svg>
        <span>danielle@wrenfieldacres.com</span>
      </p>
    </div>
  </section>
</main>
</body>
</html>
```